Willowmere Spa and Beauty Ltd. (Name of business)

I need a business card designed for this new company based out of Toronto Ontario. We specialize in Eyelash Extensions, Manicures and Pedicures, body waxing, massages, laser hair removal and botox treatments. Also offer a variety of products for sale, such as skin cream serums, collagen gel, eye cream, etc. It is a safe relaxing and non-judgemental environnment. Clients are welcome to come be pampered for the half or full day. Many service packages to choose from.

Open 7days per week from 8am to 8pm.

Marissa Thornbury
Spa Facilitator
Willowmere Spa and Beauty Ltd.
7200 Calder Ave; Suite 1400
Toronto ON K8P 2W7

OFFICE: 416.739.4100
FAX: 416.739.4101
CELL: 416.582.6074
EMAIL: marissa.thornbury@willowmerespa.example

Target Market(s)

Target market is primarily female ranging from 16 years old to 50 years old.

Industry/Entity Type

Business

Contact Information for Business Card

Marissa Thornbury
Spa Facilitator
7200 Calder Ave; Suite 1400
Toronto ON K8P 2W7

OFFICE: 416.739.4100
FAX: 416.739.4101
CELL: 416.582.6074

Logo Text

I dont have a logo yet. I would like it simple but sophisticated and modern.

Font styles to use
Serif

Requirements
Must have
• all pertinent details such as company name, logo, name and contact information, services that are offered, including package rates
Nice to have
• Company name and logo prominent. A card that is neat and the information such as address, phone number, fax, email, etc is not too crowded but laid out in an easy to read format.
• Possibly on the back of card - some of the services offered could be listed, as well as professional cream lotions and serums. Hours of operation etc.

```html
<!DOCTYPE html>
<html lang="en">
<head>
<meta charset="utf-8">
<title>Willowmere Spa and Beauty Ltd. – Business Card</title>
<link rel="stylesheet" href="https://fonts.googleapis.com/css2?family=Exo+2:wght@400;500;600&display=swap">
<style>
  :root {
    --backdrop: #f1eef0;
    --card-light: #ffffff;
    --card-shade: #e6e6e6;
    --pink: #e6588a;
    --pink-deep: #e0517f;
    --ink: #111111;
    --art-light: #e6e6e6;
    --art-mid: #b9b9b9;
    --art-dark: #1a1a1a;
  }
  * { box-sizing: border-box; margin: 0; padding: 0; }
  html, body {
    width: 1200px; height: 766px; overflow: hidden;
    background: var(--backdrop);
    font-family: "Exo 2", "Trebuchet MS", sans-serif;
  }
  .canvas { position: relative; width: 1200px; height: 766px; }
  .card {
    position: absolute; top: 230px; width: 540px; height: 306px;
    background: linear-gradient(200deg, var(--card-light) 10%, var(--card-shade) 100%);
    overflow: hidden;
  }
  .card::before, .card::after {
    content: ""; position: absolute; left: 0; right: 0; background: var(--pink); z-index: 2;
  }
  .card::before { top: 0; height: 8px; }
  .card::after { bottom: 0; height: 8px; }
  .card--front { left: 40px; }
  .card--back { left: 620px; }

  .corner { position: absolute; inset: 0; width: 540px; height: 306px; }

  .brand {
    position: absolute; left: 0; right: 0; top: 100px;
    display: flex; align-items: center; justify-content: center; gap: 14px;
  }
  .brand__dot { width: 34px; height: 34px; border-radius: 50%; background: var(--ink); }
  .brand__name {
    font-size: 46px; font-weight: 600; color: var(--ink); line-height: 1;
    letter-spacing: -0.5px;
  }
  .brand__sub {
    position: absolute; left: 0; right: 0; top: 154px; text-align: center;
    font-size: 15px; font-weight: 600; color: var(--ink); letter-spacing: 0.5px;
  }

  .services {
    position: absolute; left: 0; right: 0; top: 230px; text-align: center;
    color: var(--pink); font-size: 13px; line-height: 16px;
  }
  .services__title {
    display: flex; align-items: center; justify-content: center; gap: 6px;
    margin-bottom: 1px;
  }
  .services__title::before, .services__title::after {
    content: ""; width: 92px; height: 2px; background: var(--pink);
  }

  .portrait {
    position: absolute; left: 0; top: 8px; width: 240px; height: 290px;
    background: linear-gradient(100deg, var(--art-dark) 0%, var(--art-mid) 30%, var(--art-light) 55%, var(--art-mid) 80%, var(--art-dark) 100%);
  }
  .divider {
    position: absolute; left: 250px; top: 14px; width: 3px; height: 276px; background: var(--pink);
  }
  .contact {
    position: absolute; right: 26px; top: 20px; text-align: right; color: var(--pink);
  }
  .mark {
    display: flex; align-items: center; justify-content: flex-end; gap: 8px;
    margin-bottom: 12px;
  }
  .mark__ring { width: 40px; height: 40px; border-radius: 50%; border: 2px solid var(--ink); }
  .mark__name { font-size: 15px; font-weight: 500; color: var(--ink); }
  .contact__name { font-size: 22px; font-weight: 600; line-height: 1.1; letter-spacing: 0.3px; }
  .contact__role { font-size: 13px; margin-bottom: 18px; }
  .contact__company { font-size: 13px; font-weight: 600; line-height: 15px; }
  .contact__address { font-size: 13px; line-height: 15px; margin-bottom: 10px; }
  .contact__lines { font-size: 13px; line-height: 15.5px; margin-bottom: 10px; }
  .contact__email { font-size: 12.5px; }
</style>
</head>
<body>
<main class="canvas">

  <section class="card card--front" aria-label="Card front">
    <svg class="corner" viewBox="0 0 540 306" aria-hidden="true">
      <polygon points="0,8 130,8 0,112" fill="var(--pink-deep)"/>
      <polygon points="122,8 138,8 0,122 0,112" fill="#ffffff"/>
      <polygon points="540,202 540,298 425,298" fill="var(--pink-deep)"/>
      <polygon points="540,194 540,202 425,298 412,298" fill="#ffffff"/>
    </svg>
    <div class="brand">
      <span class="brand__dot"></span>
      <span class="brand__name">Willowmere</span>
    </div>
    <div class="brand__sub">SPA &amp; BEAUTY LTD.</div>
    <div class="services">
      <div class="services__title">SERVICES</div>
      <p>Eyelash Extensions | Manicures and Pedicures |</p>
      <p>Body waxing | Massages | Laser Hair Removal |</p>
      <p>Botox Treatments.</p>
    </div>
  </section>

  <section class="card card--back" aria-label="Card back">
    <div class="portrait" role="img" aria-label="Illustration area: stylised black-and-white beauty artwork with pink accent"></div>
    <div class="divider"></div>
    <div class="contact">
      <div class="mark">
        <span class="mark__ring"></span>
        <span class="mark__name">Willowmere</span>
      </div>
      <h1 class="contact__name">MARISSA THORNBURY</h1>
      <p class="contact__role">Spa Facilitator</p>
      <p class="contact__company">WILLOWMERE Spa &amp; Beauty Ltd.</p>
      <p class="contact__address">7200 Calder Ave; Suite 1400<br>Toronto ON K8P 2W7</p>
      <p class="contact__lines">cell | 416.582.6074<br>office | 416.739.4100<br>fax | 416.739.4101</p>
      <p class="contact__email">marissa.thornbury@willowmerespa.example</p>
    </div>
  </section>

</main>
</body>
</html>
```